Travel Group 'Lydgate Group' needs a new business card design

Lydgate Group is a diverse business specialising in bespoke, tailor made holidays to suit all budgets and we are specialists in planning exciting day/short trips to suit all markets. Our target market is very varied going from the corporate client and as well as people in the community who simply want to experience something special.
We are looking for a card design that will encourage people to look at our websites and social media platforms and to see for themselves the different facets to our business. It is essential that the card has social media icons for social profile one, social profile two and social profile three. We are looking for a card with a blank background with no pictures and for the front side to have the attached Lydgate logo. The card should have similar colour scheme to the attached Lydgate logo.
The card must have the following information on one side:
Maud Penrose
Business Development Manager
maudpenrose@lydgatevoyages.example
Lydgate Group, 87 Quarry Lane
Brackenford, Dunmere, Scotland KA19 4TN
+44 (0)1294 730182
And then the card must have the following on the second side:
(Lydgate logo)
(social media icons)
www.lydgatevoyages.example
www.lydgateoutings.example
Target Market(s)
Our target market is very varied going from the corporate client and as well as people in the community who simply want to experience something special.
Industry/Entity Type
Business
Contact Information for Business Card
Maud Penrose
+44 (0)1294 730182
(Lydgate logo)
(social media icons)
www.lydgatevoyages.example
www.lydgateoutings.example
Requirements
Must have
- It is essential that the card has social media icons for social profile one, social profile two & social profile three.
Should not have
- Should not have any images other than Lydgate logo.

```html
<!DOCTYPE html>
<html lang="en">
<head>
<meta charset="utf-8">
<title>Lydgate Group business card</title>
<link href="https://fonts.googleapis.com/css2?family=Tinos:wght@400;700&family=Roboto:wght@400&display=swap" rel="stylesheet">
<style>
  :root {
    --bg: #ecebef;
    --paper: #ffffff;
    --navy: #2a1f66;
    --magenta: #d0107f;
    --violet: #6b1e8c;
    --ink-light: #ffffff;
  }
  * { margin: 0; padding: 0; box-sizing: border-box; }
  html, body { width: 1200px; height: 911px; overflow: hidden; background: var(--bg); }
  .canvas { position: relative; width: 1200px; height: 911px; }
  .card {
    position: absolute; top: 75px; width: 440px; height: 760px;
    background: var(--paper); border-radius: 24px; overflow: hidden;
    box-shadow: 0 10px 30px rgba(40, 20, 70, 0.18);
  }
  .card--front { left: 120px; }
  .card--back { left: 640px; }

  .brand-name {
    font-family: "Tinos", serif; font-weight: 700; color: var(--navy);
    letter-spacing: 4px; text-align: center;
  }
  .card--front .brand-name { position: relative; margin-top: 56px; font-size: 40px; }
  .holder { position: relative; text-align: center; margin-top: 26px; font-family: "Tinos", serif; }
  .holder-name { font-size: 24px; font-weight: 700; color: var(--navy); letter-spacing: 1px; }
  .holder-role { font-size: 17px; color: var(--magenta); margin-top: 2px; }

  .colour-field { position: absolute; left: 0; top: 0; width: 440px; height: 760px; }

  .contact-list {
    position: absolute; left: 20px; right: 20px; top: 410px;
    list-style: none; text-align: center;
    font-family: "Roboto", sans-serif; font-size: 17px; color: var(--ink-light); line-height: 1.3;
  }
  .contact-list li { margin-bottom: 8px; }
  .contact-list svg { display: block; margin: 0 auto 3px; width: 14px; height: 14px; }
  .contact-list .address { margin-top: 2px; }

  .side-rule {
    position: absolute; left: 70px; top: 40px; width: 1px; height: 680px; background: var(--navy); opacity: 0.7;
  }
  .social-list {
    position: absolute; left: 50px; top: 300px; list-style: none;
  }
  .social-list li {
    width: 40px; height: 40px; margin-bottom: 14px; border-radius: 50%;
    border: 2px solid var(--navy); background: var(--paper);
  }
  .back-brand {
    position: absolute; left: 120px; right: 40px; top: 340px;
    display: flex; align-items: center; justify-content: center; gap: 14px;
  }
  .back-brand .brand-name { font-size: 46px; }
  .brand-dot { flex: none; width: 22px; height: 22px; border-radius: 50%; background: var(--magenta); }
</style>
</head>
<body>
<main class="canvas">
  <section class="card card--front">
    <svg class="colour-field" viewBox="0 0 440 760" aria-hidden="true">
      <defs>
        <radialGradient id="field-gradient" cx="0.45" cy="0.45" r="0.75">
          <stop offset="0" stop-color="#d0107f"/>
          <stop offset="0.55" stop-color="#8a1a8f"/>
          <stop offset="1" stop-color="#2a1f66"/>
        </radialGradient>
      </defs>
      <path d="M0,330 C110,250 250,250 320,330 C350,365 395,372 440,360 L440,760 L0,760 Z" fill="url(#field-gradient)"/>
    </svg>
    <h1 class="brand-name">LYDGATE</h1>
    <div class="holder">
      <p class="holder-name">MAUD PENROSE</p>
      <p class="holder-role">Business Development Manager</p>
    </div>
    <ul class="contact-list">
      <li><svg viewBox="0 0 14 14"><path d="M3 1l2 3-1.2 1.2a8 8 0 0 0 5 5L10 9l3 2-1 2.2C6 13 1 8 1 2z" fill="#fff"/></svg>+44 (0)1632 730182</li>
      <li><svg viewBox="0 0 14 14"><rect x="1" y="3" width="12" height="8" fill="#fff"/><path d="M1 3l6 5 6-5" stroke="#8a1a8f" fill="none"/></svg>maudpenrose@lydgatevoyages.example</li>
      <li><svg viewBox="0 0 14 14"><circle cx="7" cy="7" r="6" fill="#fff"/><path d="M1 7h12M7 1c3 3 3 9 0 12M7 1c-3 3-3 9 0 12" stroke="#8a1a8f" fill="none"/></svg>www.lydgatevoyages.example</li>
      <li><svg viewBox="0 0 14 14"><circle cx="7" cy="7" r="6" fill="#fff"/><path d="M1 7h12M7 1c3 3 3 9 0 12M7 1c-3 3-3 9 0 12" stroke="#8a1a8f" fill="none"/></svg>www.lydgateoutings.example</li>
      <li class="address"><svg viewBox="0 0 14 14"><path d="M7 13C3 8 2 6.5 2 5a5 5 0 0 1 10 0c0 1.5-1 3-5 8z" fill="#fff"/><circle cx="7" cy="5" r="1.8" fill="#6b1e8c"/></svg>Lydgate Group, 87 Quarry Lane<br>Brackenford, Dunmere, Scotland KA19 4TN</li>
    </ul>
  </section>

  <section class="card card--back">
    <div class="side-rule"></div>
    <ul class="social-list">
      <li role="img" aria-label="Social profile link one"></li>
      <li role="img" aria-label="Social profile link two"></li>
      <li role="img" aria-label="Social profile link three"></li>
    </ul>
    <div class="back-brand">
      <span class="brand-dot"></span>
      <h2 class="brand-name">LYDGATE</h2>
    </div>
  </section>
</main>
</body>
</html>
```